Funky Cup design on our hot disposable cups

I would like two examples: one orange cup (like our logo color) with white writing, one white cup with orange writing:
On the top: Organic coffee because we care
Middle: Our logo (attached but drop the R in the circle)
Bottom: Live Life Like a Tinker
Would love ideas what else can be written or patterned around the cup, clever design such as Coffee moorings or any other funky ideas.

It should include the text "tinkers & tide " all over the cup around the logo!

thanks.

Target Market(s)

female and male 17 to 30s

Industry/Entity Type

Coffee

Font styles to use
Other font styles liked:
• Galano grotesque like our logosame as logo

Colors
EE7325
F08F49
F5BC92
FAE3D3
FDF4ED

Requirements
Must have
• cool fun , trendy look. It should include the text "tinkers & tide " all over the cup around the logo!
Should not have
• in my logo please drop the r with the circle

```html
<!DOCTYPE html>
<html lang="en">
<head>
<meta charset="utf-8">
<title>tinkers &amp; tide — cup wraps</title>
<link rel="stylesheet" href="https://fonts.googleapis.com/css2?family=Poppins:wght@600;700&family=Caveat:wght@500&display=swap">
<style>
  :root {
    --orange: #EE7325;
    --white: #FFFFFF;
    --backdrop: #E8E8E8;
  }
  * { box-sizing: border-box; margin: 0; padding: 0; }
  html, body {
    width: 800px;
    height: 1200px;
    overflow: hidden;
    background: var(--backdrop);
  }
  .canvas {
    width: 800px;
    height: 1200px;
    display: flex;
    flex-direction: column;
    align-items: center;
    justify-content: center;
    gap: 40px;
  }
  .wrap {
    width: 352px;
    height: 540px;
    display: flex;
    flex-direction: column;
    align-items: center;
    justify-content: space-between;
    padding: 52px 0 50px;
    font-family: "Poppins", sans-serif;
    text-align: center;
  }
  .wrap--white { background: var(--white); color: var(--orange); }
  .wrap--orange { background: var(--orange); color: var(--white); }

  .headline { display: flex; flex-direction: column; align-items: center; }
  .headline__small {
    font-weight: 600;
    font-size: 24px;
    line-height: 1;
  }
  .headline__big {
    font-weight: 700;
    font-size: 84px;
    line-height: 0.8;
    letter-spacing: -1px;
  }
  .headline__big--first { margin-top: 8px; }
  .headline__joiner {
    font-weight: 600;
    font-size: 15px;
    line-height: 1;
    margin: 0 0 -2px;
    position: relative;
    z-index: 1;
  }

  .brand { display: block; }
  .brand__dot { fill: currentColor; }
  .brand__ring {
    fill: currentColor;
    font-family: "Poppins", sans-serif;
    font-weight: 700;
    font-size: 16px;
  }

  .tagline { display: flex; flex-direction: column; align-items: center; }
  .tagline__text {
    font-family: "Caveat", cursive;
    font-weight: 500;
    font-size: 40px;
    line-height: 1;
  }
  .tagline__rule { margin-top: 4px; display: block; }
</style>
</head>
<body>
<main class="canvas">

  <section class="wrap wrap--white" aria-label="White cup wrap with orange lettering">
    <div class="headline">
      <span class="headline__small">organic</span>
      <span class="headline__big headline__big--first">coffee</span>
      <span class="headline__joiner">because we</span>
      <span class="headline__big">care</span>
    </div>
    <svg class="brand" width="150" height="150" viewBox="0 0 150 150" aria-label="tinkers &amp; tide">
      <defs>
        <path id="ring-white" d="M75 20 a55 55 0 1 1 -0.01 0"/>
      </defs>
      <circle class="brand__dot" cx="75" cy="75" r="30"/>
      <text class="brand__ring"><textPath href="#ring-white" textLength="340" lengthAdjust="spacing">tinkers &amp; tide • tinkers &amp; tide •</textPath></text>
    </svg>
    <div class="tagline">
      <span class="tagline__text">Live Life Like a Tinker</span>
      <svg class="tagline__rule" width="230" height="10" viewBox="0 0 230 10">
        <path d="M4 6 Q115 1 226 5" fill="none" stroke="var(--orange)" stroke-width="3" stroke-linecap="round"/>
      </svg>
    </div>
  </section>

  <section class="wrap wrap--orange" aria-label="Orange cup wrap with white lettering">
    <div class="headline">
      <span class="headline__small">organic</span>
      <span class="headline__big headline__big--first">coffee</span>
      <span class="headline__joiner">because we</span>
      <span class="headline__big">care</span>
    </div>
    <svg class="brand" width="150" height="150" viewBox="0 0 150 150" aria-label="tinkers &amp; tide">
      <defs>
        <path id="ring-orange" d="M75 20 a55 55 0 1 1 -0.01 0"/>
      </defs>
      <circle class="brand__dot" cx="75" cy="75" r="30"/>
      <text class="brand__ring"><textPath href="#ring-orange" textLength="340" lengthAdjust="spacing">tinkers &amp; tide • tinkers &amp; tide •</textPath></text>
    </svg>
    <div class="tagline">
      <span class="tagline__text">Live Life Like a Tinker</span>
      <svg class="tagline__rule" width="230" height="10" viewBox="0 0 230 10">
        <path d="M4 6 Q115 1 226 5" fill="none" stroke="var(--white)" stroke-width="3" stroke-linecap="round"/>
      </svg>
    </div>
  </section>

</main>
</body>
</html>
```